Paddock Guard Solutions Business Cards and Logo

I am commencing a niche safety business for horse racing stables and breeders. The registered business name is 'Paddock Guard Solutions'. It is a business of TOVEN Advisory. The page on my website www.tovenadvisory.com.au outlines the services offered.

The most important aspect is the development of a simple logo. I envisage a logo something like three horse heads in a simple outline to form the letter E for Paddock Guard Solutions. Alternatively a simple line drawing of a horse head that might be used on stationery and merchandise for example, a logo that might be used on a polo shirt and bumber stickers.

Industry/Entity Type

Business

Contact Information for Business Card

Dennis Holbrook
Director
Paddock Guard Solutions
'Good stables are safe stables'
A business of TOVEN Advisory
0498 316 205
dennis@tovenadvisory.com.au
www.tovenadvisory.com.au

Requirements
Must have
• Logo (see above)
Name: Dennis Holbrook
Title: Director
Business Name: Paddock Guard Solutions
Motto: 'Good stables are safe stables'
A business of TOVEN Advisory (smaller print and probably ilalicised)
Phone: 0498 316 205
Email: dennis@tovenadvisory.com.au
Web Address: www.tovenadvisory.com.au

```html
<!DOCTYPE html>
<html lang="en">
<head>
<meta charset="utf-8">
<title>Paddock Guard Solutions – Business Cards</title>
<link rel="stylesheet" href="https://fonts.googleapis.com/css2?family=Open+Sans:ital,wght@0,400;0,600;0,700;1,400&display=swap">
<style>
  :root {
    --backdrop: #2b2b2d;
    --sky: #56c8ef;
    --sky-deep: #3fb6e2;
    --paper: #ffffff;
    --crimson: #e0173e;
    --shadow: rgba(0, 0, 0, 0.45);
  }
  * { box-sizing: border-box; margin: 0; padding: 0; }
  html, body {
    width: 1200px; height: 809px; overflow: hidden;
    background: var(--backdrop);
    font-family: "Open Sans", Arial, sans-serif;
  }
  .stage {
    width: 1200px; height: 809px;
    display: flex; align-items: center; justify-content: center; gap: 60px;
  }
  .card {
    width: 520px; height: 297px;
    border-radius: 3px;
    box-shadow: 0 14px 30px var(--shadow);
    display: flex; flex-direction: column; align-items: center;
    text-align: center;
  }
  .card--front { background: var(--sky); color: var(--paper); padding-top: 62px; }
  .card--back { background: var(--paper); padding-top: 40px; }

  .brand { display: flex; align-items: center; gap: 10px; }
  .brand__dot { width: 14px; height: 14px; border-radius: 50%; background: currentColor; }
  .brand__name { font-weight: 700; font-size: 30px; letter-spacing: 0.5px; line-height: 1.1; }
  .brand__parent { font-style: italic; font-size: 12px; margin-top: 6px; }

  .card--back .brand, .card--back .brand__parent { color: var(--sky-deep); }
  .card--back .brand__name { font-size: 26px; }

  .motto { font-style: italic; font-size: 25px; margin-top: 26px; }

  .person { margin-top: 24px; }
  .person__name { color: var(--crimson); font-weight: 700; font-size: 21px; line-height: 1.2; }
  .person__role { color: var(--sky-deep); font-size: 15px; }

  .contacts { list-style: none; margin-top: 12px; text-align: left; }
  .contacts li {
    display: flex; align-items: center; gap: 8px;
    color: var(--crimson); font-weight: 600; font-size: 16px; line-height: 1.55;
  }
  .contacts svg { width: 16px; height: 16px; flex: none; stroke: var(--sky-deep); fill: none; stroke-width: 1.6; }
</style>
</head>
<body>
<main class="stage">
  <section class="card card--front">
    <div class="brand">
      <span class="brand__dot"></span>
      <span class="brand__name">Paddock Guard Solutions</span>
    </div>
    <p class="brand__parent">A Business of TOVEN Advisory</p>
    <p class="motto">“Good stables are safe stables”</p>
  </section>

  <section class="card card--back">
    <div class="brand">
      <span class="brand__dot"></span>
      <span class="brand__name">Paddock Guard Solutions</span>
    </div>
    <p class="brand__parent">A business of TOVEN Advisory</p>

    <div class="person">
      <p class="person__name">Dennis Holbrook</p>
      <p class="person__role">Director</p>
    </div>

    <ul class="contacts">
      <li>
        <svg viewBox="0 0 16 16" aria-hidden="true"><path d="M4 1.5l2.5 3-1.5 1.8c.8 1.7 2 2.9 3.7 3.7L10.5 8.5l3 2.5-1.5 3C7 13.5 2.5 9 2 4z"/></svg>
        0498 316 205
      </li>
      <li>
        <svg viewBox="0 0 16 16" aria-hidden="true"><rect x="1.5" y="3.5" width="13" height="9"/><path d="M1.5 3.5L8 9l6.5-5.5"/></svg>
        dennis@tovenadvisory.com.au
      </li>
      <li>
        <svg viewBox="0 0 16 16" aria-hidden="true"><circle cx="8" cy="8" r="6.5"/><ellipse cx="8" cy="8" rx="2.8" ry="6.5"/><path d="M1.5 8h13"/></svg>
        www.tovenadvisory.com.au
      </li>
    </ul>
  </section>
</main>
</body>
</html>
```